Come as U R - mental health service LGBTIQ inclusive poster

We are a mental health organisation in Australia that is looking for a poster design that we can put in our waiting rooms to show that our service is inclusive of gender diverse, intersex, and sexuality diverse people. We will add text and our company logo afterwards. An example has been provided for inspiration. Designers 25 and under encouraged.

Target Market(s)

Target audience - all genders 12-25.

Industry/Entity Type

Mental Health

Requirements
Must have
• This graphic should be colourful, include the text "Come as U R", and incorporate the colours of the pride flag. Should be a general design that is appropriate for all of the target audience.

```html
<!DOCTYPE html>
<html lang="en">
<head>
<meta charset="utf-8">
<title>Come as U R – Inclusive Service Poster</title>
<link rel="stylesheet" href="https://fonts.googleapis.com/css2?family=Alfa+Slab+One&display=swap">
<style>
  :root {
    --steel-light: #a3a6aa;
    --steel-mid: #8c8f93;
    --steel-dark: #76797d;
    --emblem-white: #ffffff;
    --emblem-cream: #f4efe6;
    --ink: #262626;
    --pride-red: #e8423a;
    --pride-orange: #f39a3c;
    --pride-yellow: #f4dc4a;
    --pride-green: #6cc04a;
    --pride-blue: #4a7fd0;
    --pride-purple: #7a55b0;
  }
  html, body {
    margin: 0;
    padding: 0;
    overflow: hidden;
  }
  .poster {
    position: relative;
    width: 960px;
    height: 1200px;
    overflow: hidden;
    background: linear-gradient(180deg, var(--steel-light) 0%, var(--steel-mid) 55%, var(--steel-dark) 100%);
    font-family: "Alfa Slab One", "Rockwell", serif;
  }
  .rainbow-wash {
    position: absolute;
    inset: 0;
    background: linear-gradient(135deg,
      var(--pride-purple) 0%,
      var(--pride-blue) 14%,
      var(--pride-green) 26%,
      var(--pride-yellow) 38%,
      var(--pride-orange) 48%,
      var(--pride-red) 56%,
      var(--pride-purple) 66%,
      var(--pride-blue) 74%,
      var(--pride-green) 82%,
      var(--pride-yellow) 90%,
      var(--pride-orange) 100%);
    opacity: 0.85;
    -webkit-mask-image: radial-gradient(ellipse 75% 55% at 55% 38%, #000 55%, transparent 100%);
    mask-image: radial-gradient(ellipse 75% 55% at 55% 38%, #000 55%, transparent 100%);
  }
  .emblem-area {
    position: absolute;
    left: 150px;
    top: 170px;
    width: 660px;
    height: 590px;
    border-radius: 48%;
    background: radial-gradient(ellipse at 50% 45%, var(--emblem-white) 0%, var(--emblem-white) 55%, var(--emblem-cream) 80%, rgba(244, 239, 230, 0) 100%);
  }
  .headline {
    position: absolute;
    left: 150px;
    top: 170px;
    width: 660px;
    height: 590px;
    margin: 0;
    display: flex;
    flex-direction: column;
    align-items: center;
    justify-content: center;
    color: var(--ink);
    font-weight: 400;
    font-size: 110px;
    line-height: 1.1;
    letter-spacing: 2px;
    text-align: center;
  }
</style>
</head>
<body>
<main class="poster">
  <div class="rainbow-wash" role="img" aria-label="Diagonal crayon strokes in the pride flag colours"></div>
  <div class="emblem-area" role="img" aria-label="White sketched heart emblem with pride colour outline"></div>
  <h1 class="headline">
    <span class="line">COME</span>
    <span class="line">AS U R</span>
  </h1>
</main>
</body>
</html>
```